3 x 3 metre trade booth design

We need a design for a 3 x 3 metre corner booth for a conference we are attending. There will therefore be 2 x backdrops that we need to have designed. For one of them we want to have our services displayed as an engaging, modern infographic. For the other, we would like to have our brand tagline and our logo, with a cool background which aligns with what we do.
I have attached a picture of what our booth looked like last year- we designed this ourself and we need it to look much more professional, with a different type of infographic for the
Please see attachment with full design brief attached

```html
<!DOCTYPE html>
<html lang="en">
<head>
<meta charset="utf-8">
<title>Vantora – Booth Backdrops</title>
<link href="https://fonts.googleapis.com/css2?family=Montserrat:wght@400;500;600;700;800&family=Oswald:wght@300;400&display=swap" rel="stylesheet">
<style>
  :root {
    --stage: #2f2f2f;
    --purple: #9c5fa2;
    --mauve: #b98488;
    --tan: #d1a170;
    --gold: #f0c832;
    --ink: #2a2226;
    --white: #ffffff;
    --card-top: #a56ba6;
    --card-bottom: #b77f9a;
    --dot-line: rgba(60, 40, 50, 0.75);
  }
  * { margin: 0; padding: 0; box-sizing: border-box; }
  html, body { width: 982px; height: 1200px; overflow: hidden; background: var(--stage); }
  body { font-family: "Montserrat", sans-serif; color: var(--white); }

  .stage { position: relative; width: 982px; height: 1200px; }
  .backdrop-slot { position: absolute; left: 141px; width: 700px; height: 561px; overflow: hidden; }
  .backdrop-slot.brand-slot { top: 26px; }
  .backdrop-slot.services-slot { top: 613px; }

  .backdrop {
    position: absolute; left: 0; top: 0;
    width: 786px; height: 630px;
    transform: scale(0.8906); transform-origin: 0 0;
    background: linear-gradient(150deg, var(--purple) 0%, var(--mauve) 30%, var(--tan) 62%, var(--gold) 100%);
  }

  /* Brand panel */
  .brand-lockup { position: absolute; left: 141px; top: 84px; display: flex; align-items: center; gap: 12px; }
  .brand-lockup .brand-square { width: 22px; height: 22px; background: var(--white); }
  .brand-name { font-weight: 800; font-size: 27px; letter-spacing: 5px; line-height: 1; }
  .brand-descriptor { position: absolute; left: 180px; top: 113px; font-size: 12px; font-weight: 500; letter-spacing: 0.5px; }

  .tagline { position: absolute; left: 97px; top: 172px; }
  .tagline-lead { font-size: 24px; font-weight: 500; letter-spacing: 0.5px; line-height: 1.1; }

  .highlight-box {
    display: inline-block; margin-top: 4px;
    background: var(--ink); border: 2px solid var(--gold); border-radius: 3px;
    padding: 1px 6px 2px;
  }
  .highlight-text {
    font-weight: 700; letter-spacing: 0.5px;
    background: linear-gradient(90deg, var(--gold) 0%, #d7a84a 45%, #a565b0 100%);
    -webkit-background-clip: text; background-clip: text; color: transparent;
  }
  .tagline .highlight-text { font-size: 24px; }

  /* Services panel */
  .services-heading { position: absolute; left: 0; right: 0; top: 52px; text-align: center; }
  .services-heading .heading-lead { font-size: 28px; font-weight: 500; letter-spacing: 0.8px; line-height: 1.1; }
  .services-heading .highlight-text { font-size: 28px; }
  .services-heading .highlight-box { margin-top: 1px; padding: 0 6px; }

  .service { position: absolute; border: 1.2px dashed var(--dot-line); border-radius: 10px; }
  .service .card {
    position: absolute; left: 6px; top: 6px; right: 6px; bottom: 6px;
    border-radius: 8px;
    background: linear-gradient(180deg, var(--card-top), var(--card-bottom));
    box-shadow: 0 2px 4px rgba(80, 40, 70, 0.25);
  }
  .service-content { position: absolute; left: 0; right: 0; text-align: center; padding: 0 8px; }
  .service-icon { display: block; margin: 0 auto 6px; width: 26px; height: 26px; }
  .service-title { font-size: 11px; font-weight: 700; line-height: 1.2; letter-spacing: 0.3px; }
  .service-points { margin-top: 7px; list-style: none; font-family: "Oswald", sans-serif; font-weight: 300; font-size: 7.4px; line-height: 1.45; letter-spacing: 0.1px; white-space: nowrap; }
  .node { position: absolute; width: 5px; height: 5px; border-radius: 50%; background: var(--ink); top: 50%; margin-top: -2.5px; }
  .node.left { left: -3px; }
  .node.right { right: -3px; }

  .svc-setup { left: 58px; top: 176px; width: 136px; height: 154px; }
  .svc-setup .service-content { top: 30px; }
  .svc-account { left: 194px; top: 240px; width: 132px; height: 130px; border-top: none; border-top-left-radius: 0; border-top-right-radius: 0; }
  .svc-account .service-content { top: 8px; }
  .svc-ads { left: 326px; top: 148px; width: 132px; height: 150px; }
  .svc-ads .service-content { top: 24px; }
  .svc-global { left: 458px; top: 240px; width: 134px; height: 130px; border-top: none; border-top-left-radius: 0; border-top-right-radius: 0; }
  .svc-global .service-content { top: 8px; }
  .svc-content { left: 592px; top: 180px; width: 132px; height: 150px; }
  .svc-content .service-content { top: 26px; }
</style>
</head>
<body>
<main class="stage">

  <section class="backdrop-slot brand-slot" aria-label="Brand backdrop">
    <div class="backdrop brand-backdrop">
      <div class="brand-lockup">
        <span class="brand-square" aria-hidden="true"></span>
        <span class="brand-name">VANTORA</span>
      </div>
      <p class="brand-descriptor">ARCADA MASTERY AGENCY</p>
      <div class="tagline">
        <p class="tagline-lead">TRANSFORMING BRANDS INTO</p>
        <p class="highlight-box"><span class="highlight-text">ARCADA SUCCESS STORIES</span></p>
      </div>
    </div>
  </section>

  <section class="backdrop-slot services-slot" aria-label="Services backdrop">
    <div class="backdrop services-backdrop">
      <header class="services-heading">
        <p class="heading-lead">FULL SERVICE</p>
        <p class="highlight-box"><span class="highlight-text">MANAGEMENT</span></p>
      </header>

      <article class="service svc-setup">
        <span class="node left"></span>
        <div class="card"></div>
        <div class="service-content">
          <svg class="service-icon" viewBox="0 0 26 26" fill="none" stroke="#fff" stroke-width="1.8" stroke-linecap="round" stroke-linejoin="round">
            <path d="M3 5h3l3 11h11l2-8H8"/><circle cx="11" cy="20" r="1.6" fill="#fff"/><circle cx="18" cy="20" r="1.6" fill="#fff"/><path d="M14 3v7M11.5 7.5 14 10l2.5-2.5"/>
          </svg>
          <h3 class="service-title">ARCADA<br>ACCOUNT SETUP</h3>
          <ul class="service-points">
            <li>COST ANALYSIS TO SCALE PROFITABLY</li>
            <li>ARCADA ACCOUNT SETUP</li>
            <li>ACCOUNT AUDIT</li>
            <li>BRAND PROTECTION</li>
          </ul>
        </div>
      </article>

      <article class="service svc-account">
        <div class="service-content">
          <svg class="service-icon" viewBox="0 0 26 26" fill="none" stroke="#fff" stroke-width="1.8">
            <circle cx="13" cy="13" r="4"/><circle cx="13" cy="13" r="8" stroke-dasharray="3 2.3" stroke-width="3"/>
          </svg>
          <h3 class="service-title">ACCOUNT<br>MANAGEMENT</h3>
          <ul class="service-points">
            <li>CATALOGUE MANAGEMENT</li>
            <li>ACCOUNT HEALTH MONITORING</li>
            <li>CASE LOG &amp; ISSUE RESOLUTION</li>
            <li>INVENTORY &amp; STOCK PLANNING</li>
            <li>CUSTOMISED REPORTING</li>
          </ul>
        </div>
      </article>

      <article class="service svc-ads">
        <div class="card"></div>
        <div class="service-content">
          <svg class="service-icon" viewBox="0 0 26 26" fill="none" stroke="#fff" stroke-width="1.8">
            <ellipse cx="9" cy="9" rx="6" ry="4"/><ellipse cx="17" cy="16" rx="6" ry="4"/><path d="M3 9v2c0 2 3 4 6 4M11 16v2c0 2 3 4 6 4s6-2 6-4v-2"/>
          </svg>
          <h3 class="service-title">ARCADA<br>ADVERTISING</h3>
          <ul class="service-points">
            <li>PAID SEARCH ADS (PPC)</li>
            <li>BID AUTOMATION</li>
            <li>PROGRAMMATIC DISPLAY ADS</li>
          </ul>
        </div>
      </article>

      <article class="service svc-global">
        <div class="service-content">
          <svg class="service-icon" viewBox="0 0 26 26" fill="#fff" stroke="#fff" stroke-width="1.6" stroke-linecap="round">
            <rect x="4" y="17" width="4" height="6" stroke="none"/><rect x="10" y="13" width="4" height="10" stroke="none"/><rect x="16" y="9" width="4" height="14" stroke="none"/><path d="M4 13 17 4" fill="none"/><path d="M13 3.5h4.5V8" fill="none"/>
          </svg>
          <h3 class="service-title">INTERNATIONAL<br>EXPANSION</h3>
          <ul class="service-points">
            <li>MARKET OPPORTUNITY ANALYSIS</li>
            <li>LAUNCH IN NEW MARKETPLACES</li>
            <li>LISTING LOCALISATION</li>
            <li>LOGISTICS &amp; FULFILMENT STRATEGY</li>
          </ul>
        </div>
      </article>

      <article class="service svc-content">
        <span class="node right"></span>
        <div class="card"></div>
        <div class="service-content">
          <svg class="service-icon" viewBox="0 0 26 26">
            <path d="M13 3a10 10 0 1 0 10 10H13z" fill="#fff"/><path d="M15 1.5v9.5h9.5A9.5 9.5 0 0 0 15 1.5z" fill="#fff"/>
          </svg>
          <h3 class="service-title">BRAND CONTENT<br>&amp; OPTIMISATION</h3>
          <ul class="service-points">
            <li>RICH MEDIA PAGE CONTENT</li>
            <li>STOREFRONT DESIGN</li>
            <li>PRODUCT LISTING OPTIMISATION</li>
            <li>SEARCH OPTIMISATION (SEO)</li>
          </ul>
        </div>
      </article>
    </div>
  </section>

</main>
</body>
</html>
```